Postcard Design hearing aid sales & service. Free hearing test . Fresh batteries

Bluebonnet Hearing Aid Device Center . Located at 417 Marwick Ln Abilene Texas 79488 Ph 325-555-0147.
Hours Mon thru Thurs 9:00am - 5:00pm closed for lunch 12:00pm - 1:00pm . Fri open 9:00am - 1:00pm
Hearing Test n/c Hearing aid adjustment & cleaning of hearing aids n/c . Fresh batteries buy one 1/2 off on 2nd pack. Limited time. Walk-in welcome Appointments appreciated. THIS MONTH ONLY Special discounts on new state of the art hearing aids w/remote. .

```html
<!DOCTYPE html>
<html lang="en">
<head>
<meta charset="utf-8">
<title>Bluebonnet Hearing Aid Device Center – Postcard</title>
<link rel="stylesheet" href="https://fonts.googleapis.com/css2?family=Marcellus&family=Questrial&display=swap">
<style>
  :root {
    --page: #ffffff;
    --stage: #111416;
    --paper: #e4e0d4;
    --ink: #111111;
    --muted: #6e6d69;
    --band: #e7c21f;
    --burst: #ffdd00;
    --burst-ink: #e2262a;
    --sky-top: #dedbcd;
    --sky-low: #c6c4b2;
    --hill: #23241b;
    --hill-deep: #101110;
    --phone: #1ea6e2;
    --tag: #e5197b;
    --white: #ffffff;
  }
  * { margin: 0; padding: 0; box-sizing: border-box; }
  html, body { width: 1200px; height: 1000px; overflow: hidden; background: var(--page); }
  .board { position: relative; width: 1200px; height: 1000px; }
  .stage { position: absolute; left: 0; top: 617px; width: 1200px; height: 383px; background: var(--stage); }

  .card-front {
    position: absolute; width: 728px; height: 560px; overflow: hidden;
    background: var(--paper); font-family: "Questrial", sans-serif; transform-origin: 0 0;
  }
  .card-front.is-hero { left: 236px; top: 40px; }
  .card-front.is-thumb { left: 211px; top: 662px; transform: scale(0.518); }

  .brand-name { position: absolute; left: 37px; top: 26px; font-family: "Marcellus", serif; font-size: 44px; line-height: 1; color: var(--ink); letter-spacing: 0.5px; }
  .brand-sub { position: absolute; left: 352px; top: 32px; font-size: 27px; line-height: 1; color: var(--ink); }
  .services { position: absolute; left: 0; top: 80px; width: 100%; text-align: center; font-size: 18px; line-height: 22px; color: var(--muted); }
  .promo-band { position: absolute; left: 0; top: 129px; width: 100%; height: 22px; background: var(--band); text-align: center; font-size: 13px; line-height: 22px; color: var(--ink); }
  .scene { position: absolute; left: 0; top: 151px; width: 728px; height: 409px;
    background: linear-gradient(180deg, var(--sky-top) 0%, var(--sky-low) 38%, var(--hill) 58%, var(--hill-deep) 100%); }

  .battery-offer { position: absolute; left: 30px; top: 321px; width: 152px; height: 152px; border-radius: 50%; background: var(--burst);
    color: var(--burst-ink); font-family: "Questrial", sans-serif; text-align: center; display: flex; flex-direction: column; justify-content: center; transform: rotate(-15deg); line-height: 1.05; }
  .battery-offer .lead { font-size: 18px; }
  .battery-offer .deal { font-size: 19px; font-weight: 700; font-family: Arial, sans-serif; }
  .battery-offer .note { font-size: 13px; }

  .address { position: absolute; left: 0; top: 446px; width: 100%; text-align: center; padding-left: 0; font-size: 20px; color: var(--white); }
  .phone { position: absolute; left: 0; top: 482px; width: 100%; text-align: center; font-size: 29px; color: var(--phone); }
  .hours { position: absolute; left: 0; top: 528px; width: 100%; text-align: center; font-size: 13px; color: var(--white); }
  .hours .tag { background: var(--tag); padding: 1px 3px; }

  .card-back { position: absolute; left: 606px; top: 662px; width: 381px; height: 293px; background: var(--white); font-family: "Questrial", sans-serif; color: var(--ink); }
  .card-back .back-name { position: absolute; left: 34px; top: 8px; font-family: "Marcellus", serif; font-size: 20px; }
  .card-back .back-sub { position: absolute; left: 34px; top: 27px; font-size: 11px; }
  .card-back .back-address { position: absolute; left: 19px; top: 43px; font-size: 10px; }
  .card-back .back-phone { position: absolute; left: 49px; top: 57px; font-size: 12px; }
  .card-back .stamp { position: absolute; left: 289px; top: 5px; width: 88px; height: 88px; border: 1px solid var(--ink); }
  .card-back .divider { position: absolute; left: 184px; top: 93px; width: 1px; height: 152px; background: var(--ink); }
</style>
</head>
<body>
<div class="board">
  <div class="stage"></div>

  <section class="card-front is-hero">
    <div class="brand-name">BLUEBONNET</div>
    <div class="brand-sub">hearing aid device center</div>
    <p class="services">Hearing Test n/c Hearing aid adjustment &amp; amp cleaning of hearing aids n/c .<br>Walk-in welcome Appointments appreciated.</p>
    <div class="promo-band">THIS MONTH ONLY Special discounts on new state of the art hearing aids w/remote.</div>
    <div class="scene" role="img" aria-label="Photo: silhouettes of a child and a woman playing on a grassy hillside at dusk"></div>
    <div class="battery-offer"><span class="lead">Fresh<br>batteries</span><span class="deal">buy one 1/2<br>off on<br>2nd pack.</span><span class="note">Limited time</span></div>
    <div class="address">417 Marwick Ln Abilene Texas 79488</div>
    <div class="phone">Ph 325 - 555 - 0147</div>
    <div class="hours"><span class="tag">Open Hours</span> Mon thru Thurs 9:00am - 5:00pm&nbsp; closed for lunch 12:00pm - 1:00pm . Fri open 9:00am - 1:00pm</div>
  </section>

  <section class="card-front is-thumb">
    <div class="brand-name">BLUEBONNET</div>
    <div class="brand-sub">hearing aid device center</div>
    <p class="services">Hearing Test n/c Hearing aid adjustment &amp; amp cleaning of hearing aids n/c .<br>Walk-in welcome Appointments appreciated.</p>
    <div class="promo-band">THIS MONTH ONLY Special discounts on new state of the art hearing aids w/remote.</div>
    <div class="scene" role="img" aria-label="Photo: silhouettes of a child and a woman playing on a grassy hillside at dusk"></div>
    <div class="battery-offer"><span class="lead">Fresh<br>batteries</span><span class="deal">buy one 1/2<br>off on<br>2nd pack.</span><span class="note">Limited time</span></div>
    <div class="address">417 Marwick Ln Abilene Texas 79488</div>
    <div class="phone">Ph 325 - 555 - 0147</div>
    <div class="hours"><span class="tag">Open Hours</span> Mon thru Thurs 9:00am - 5:00pm&nbsp; closed for lunch 12:00pm - 1:00pm . Fri open 9:00am - 1:00pm</div>
  </section>

  <section class="card-back">
    <div class="back-name">BLUEBONNET</div>
    <div class="back-sub">hearing aid device center</div>
    <div class="back-address">417 Marwick Ln Abilene Texas 79488</div>
    <div class="back-phone">Ph 325 - 555 - 0147</div>
    <div class="stamp"></div>
    <div class="divider"></div>
  </section>
</div>
</body>
</html>
```